Local Flower Farm Needs Business Card Design

I need business cards designed for a flower farm based in Eudora, Kansas.
Business Info:
We are a local cut flower farm located in Eudora, Kansas, founded by Darla Hoffstrom. What started as a passion for agriculture and search for more joy in daily life has blossomed into a small business dedicated to providing the community with beautiful, fresh, and sustainable flowers. We specialize in local, seasonal blooms, ensuring that every petal reflects the care and dedication we pour into our craft. Our mission is to deliver the highest quality flowers directly to our customers through local farmers markets and to florists who share our commitment to sustainability. Join us in celebrating the beauty of nature, one bloom at a time!
Contact Details:
Darla Hoffstrom
Owner
Phone 913-555-0147
Facebook: Lorabelle Quinn Blossoms
Instagram: @LorabelleQuinnBlossoms
Website: LorabelleQuinnBlossoms.example
Target Market(s)
Wholesale to Florists and Direct to Consumer via Farmers Market
Industry/Entity Type
Florist, Farm
Contact Information for Business Card
Name, Contact Info, Logo
Look and feel

```html
<!DOCTYPE html>
<html lang="en">
<head>
<meta charset="utf-8">
<title>Lorabelle Quinn Blossoms — Business Card</title>
<link rel="stylesheet" href="https://fonts.googleapis.com/css2?family=Playfair+Display:wght@400;500&family=Lato:wght@300;400&display=swap">
<style>
  :root {
    --stage: #2a2a2a;
    --teal: #0b2a2e;
    --silver: #c9cdcf;
    --paper: #ffffff;
    --ink: #0b2a2e;
    --muted: #4a5557;
    --serif: "Playfair Display", Georgia, serif;
    --sans: "Lato", Arial, sans-serif;
  }
  * { box-sizing: border-box; margin: 0; padding: 0; }
  html, body { width: 1200px; height: 875px; overflow: hidden; background: var(--stage); }
  .stage {
    width: 1200px; height: 875px;
    display: flex; align-items: center; justify-content: center; gap: 40px;
  }
  .card {
    width: 540px; height: 309px;
    border-radius: 18px;
    position: relative;
    overflow: hidden;
  }
  /* Front */
  .card--front { background: var(--teal); display: flex; align-items: center; justify-content: center; }
  .brand-seal {
    width: 200px; height: 200px;
    border: 1.5px solid var(--silver);
    border-radius: 50%;
    display: flex; align-items: center; justify-content: center;
    text-align: center;
  }
  .brand-seal__name {
    font-family: var(--serif);
    font-weight: 400;
    color: var(--silver);
    font-size: 20px;
    line-height: 1.3;
    letter-spacing: 2px;
    text-transform: uppercase;
  }
  /* Back */
  .card--back { background: var(--paper); }
  .brand-mark {
    position: absolute; right: 34px; top: 30px;
    font-family: var(--serif);
    font-weight: 400;
    color: var(--ink);
    font-size: 44px;
    line-height: 1.05;
    text-align: right;
  }
  .contact-block { position: absolute; left: 40px; bottom: 30px; }
  .contact-block__name {
    font-family: var(--serif);
    font-weight: 500;
    color: var(--ink);
    font-size: 22px;
    line-height: 1.05;
    letter-spacing: 1px;
    text-transform: uppercase;
  }
  .contact-block__role {
    font-family: var(--sans); font-weight: 300;
    color: var(--muted); font-size: 13px; margin-top: 3px;
  }
  .contact-block__rule { width: 26px; height: 2px; background: var(--ink); margin: 10px 0 10px; }
  .contact-list { list-style: none; }
  .contact-list__item {
    display: flex; align-items: center; gap: 10px;
    font-family: var(--sans); font-weight: 400;
    color: var(--muted); font-size: 12.5px; line-height: 1.65;
  }
  .contact-list__icon { width: 10px; height: 10px; flex: none; }
  .contact-list__dot { width: 8px; height: 8px; border-radius: 50%; background: var(--ink); flex: none; margin: 0 1px; }
</style>
</head>
<body>
<main class="stage">
  <section class="card card--front" aria-label="Card front">
    <div class="brand-seal">
      <p class="brand-seal__name">Lorabelle<br>Quinn<br>Blossoms</p>
    </div>
  </section>

  <section class="card card--back" aria-label="Card back">
    <p class="brand-mark">Lorabelle<br>Quinn<br>Blossoms</p>

    <div class="contact-block">
      <h1 class="contact-block__name">Darla<br>Hoffstrom</h1>
      <p class="contact-block__role">Owner</p>
      <div class="contact-block__rule"></div>
      <ul class="contact-list">
        <li class="contact-list__item">
          <svg class="contact-list__icon" viewBox="0 0 24 24" aria-hidden="true"><path fill="#0b2a2e" d="M6.6 10.8a15.1 15.1 0 0 0 6.6 6.6l2.2-2.2a1 1 0 0 1 1-.25 11.4 11.4 0 0 0 3.6.57 1 1 0 0 1 1 1V20a1 1 0 0 1-1 1A17 17 0 0 1 3 4a1 1 0 0 1 1-1h3.5a1 1 0 0 1 1 1c0 1.25.2 2.45.57 3.6a1 1 0 0 1-.25 1z"/></svg>
          913-555-0147
        </li>
        <li class="contact-list__item"><span class="contact-list__dot"></span>Lorabelle Quinn Blossoms</li>
        <li class="contact-list__item"><span class="contact-list__dot"></span>LorabelleQuinnBlossoms</li>
        <li class="contact-list__item"><span class="contact-list__dot"></span>LorabelleQuinnBlossoms.example</li>
      </ul>
    </div>
  </section>
</main>
</body>
</html>
```